Website Design for Kids

We need to redesign our site pumblewok.net.
Current site was done long ago in Flash. We need to remove Flash and create a responsive site which can be viewed on phone, tablets as well as PC.
We are looking for a new fresh design. No elements from existing design need to be incorporated into new design.
The site is targeted for kids 7-12 years old.
Design should have attractive colors and it should be easy to navigate. It will be even better to provide one theme for boys and one for girls.
New site will have following features:
SHORT STORIES
Ability to display thumbnails of stories available. When user click a story it will play.
See http://pumblewok.net/stories/index.asp to get an idea.
MOVIES
We have two moves, more to come. Users will be able to see thumbnails and watch trailers. To watch full movie they will be redirect to a Plorvu page where they can pay and watch.
See http://pumblewok.net/Movies/ to get an idea.
PICTURE STORIES
This will feature short stories. When a story is clicked it will start playing. The stories will have picture and text, possibly audio too.
See http://pumblewok.net/stories/stories.asp to get an idea.
AUDIO STORIES
Audio stories recorded from kids or adults will be played. Optional photo of the person who recorded story will be displayed. User will have option to select a story by clicking thumbnail of stories.
VIDEO STORIES
Like audio stories, user will be able to scroll though thumbnails of stories and play one. Short video 1-3 mins will be played.
- I have upgraded budget and added a few more simple requirements. Need to decide soon so please submit your designs asap.
Number of Pages Required
5+ page

```html
<!DOCTYPE html>
<html lang="en">
<head>
<meta charset="utf-8">
<title>Pumblewok — Stories and Movies for Kids</title>
<link rel="stylesheet" href="https://fonts.googleapis.com/css2?family=Oswald:wght@500;600&family=Open+Sans:wght@400;600;700&display=swap">
<style>
:root{
  --sky-top:#f6c86a;
  --sky-mid:#f2a23e;
  --sand:#e68a2c;
  --sand-deep:#c9651d;
  --grass:#f4c640;
  --navy:#2d3f6e;
  --brand:#6a3fa0;
  --stories:#f2c227;
  --movies:#5cc3e4;
  --pictures:#c8393b;
  --ink:#2b2b2b;
  --white:#ffffff;
  --gold:#e5b53a;
  --go:#f0b323;
  --footer:#5b5fb1;
  --social-a:#3b5a9a;
  --social-b:#34aadf;
  --social-c:#d44b38;
  --trailer:#6a8c3a;
  --buy:#e4892a;
}
*{box-sizing:border-box;margin:0;padding:0}
html,body{width:1200px;height:2172px;overflow:hidden}
body{font-family:"Open Sans",Arial,sans-serif;color:var(--ink);position:relative;
  background:linear-gradient(180deg,var(--sky-top) 0,#f8dc93 300px,var(--sky-mid) 560px,var(--sand) 900px,var(--sand-deep) 1400px,var(--sand) 1800px,var(--grass) 2000px,var(--grass) 2172px)}
.abs{position:absolute}
.site-nav{left:0;top:0;width:1200px;height:110px;display:flex;justify-content:center;gap:70px;padding-top:36px}
.nav-item{display:flex;flex-direction:column;align-items:center;gap:6px;font-size:12px;font-weight:600;color:var(--white);text-transform:uppercase;letter-spacing:.5px}
.nav-item svg{width:34px;height:30px}
.social{left:0;top:222px;display:flex;flex-direction:column;gap:4px}
.social span{display:block;width:36px;height:36px}
.brand{left:0;top:290px;width:1200px;text-align:center}
.brand-name{font-family:"Open Sans",sans-serif;font-weight:700;font-size:72px;color:var(--brand)}
.signup{left:210px;top:540px;width:780px;height:110px}
.signup-bar{position:absolute;left:60px;top:24px;width:660px;height:64px;background:var(--navy);border-radius:8px;padding:8px 0 0 80px}
.signup-label{font-size:15px;font-weight:700;color:var(--white);text-transform:uppercase}
.signup-input{position:absolute;left:80px;top:32px;width:380px;height:24px;background:var(--white);border-radius:2px}
.signup-go{position:absolute;left:472px;top:30px;width:50px;height:28px;background:var(--go);border-radius:3px;color:var(--white);font-weight:700;font-size:13px;text-align:center;line-height:28px}
.mascot{position:absolute;top:0;width:110px;height:110px;border-radius:50%}
.mascot.left{left:0;background:radial-gradient(circle,#f7ddc0 55%,#f4f4f4 56%)}
.mascot.right{right:0;background:radial-gradient(circle,#f7ddc0 50%,#7fb6de 51%)}
.panel{left:180px;width:840px;border-radius:2px;padding:0 30px}
.panel h2{font-family:"Oswald",sans-serif;font-weight:600;font-size:34px;text-align:center;color:var(--ink);padding-top:16px;height:72px;text-transform:uppercase;line-height:1.2}
.panel.stories{top:720px;height:420px;background:var(--stories)}
.panel.movies{top:1170px;height:420px;background:var(--movies)}
.panel.pictures{top:1622px;height:410px;background:var(--pictures)}
.panel.pictures h2{color:var(--white)}
.thumb-grid{position:absolute;left:30px;top:80px;width:380px;display:grid;grid-template-columns:1fr 1fr;gap:14px 18px}
.thumb{display:flex;flex-direction:column;align-items:center;gap:4px}
.thumb .art{width:100%;height:100px;border:3px solid var(--white)}
.thumb .caption{font-size:10px;font-weight:700;text-transform:uppercase;color:var(--ink)}
.feature{position:absolute;left:440px;top:80px;width:370px}
.feature .art{width:100%;height:220px;border:4px solid var(--white)}
.feature .caption{text-align:center;font-size:13px;font-weight:700;text-transform:uppercase;margin-top:6px}
.dots{position:absolute;left:0;width:100%;display:flex;justify-content:center;gap:8px}
.dots i{display:block;width:10px;height:10px;border-radius:50%;background:rgba(255,255,255,.6)}
.dots i.on{background:var(--white)}
.movie-list{position:absolute;left:30px;top:80px;width:290px;display:flex;flex-direction:column;gap:24px}
.movie{display:flex;gap:14px}
.movie .poster{width:86px;height:124px;border:3px solid var(--white);flex:none}
.movie h3{font-size:12px;font-weight:700;text-transform:uppercase;line-height:1.35;color:var(--ink)}
.movie .price{font-size:12px;font-weight:700;margin-top:10px;display:flex;justify-content:space-between;width:170px}
.movie .actions{display:flex;gap:8px;margin-top:8px}
.btn{display:inline-block;width:68px;height:22px;line-height:22px;text-align:center;font-size:10px;font-weight:700;text-transform:uppercase;color:var(--white);background:var(--trailer);border-radius:2px}
.btn.buy{background:var(--buy)}
.player{position:absolute;left:330px;top:80px;width:480px;height:312px;border:10px solid var(--gold);border-radius:4px;overflow:hidden}
.player .art{position:absolute;inset:0;background:linear-gradient(180deg,#8ec6e6,#5aa3cf 60%,#c99e6a)}
.player .notice{position:absolute;right:28px;top:34px;width:170px;background:var(--white);padding:10px 12px;font-size:12px;line-height:1.4;color:var(--ink)}
.player .controls{position:absolute;left:0;right:0;bottom:0;height:36px;background:rgba(20,20,30,.8);display:flex;align-items:center;padding:0 12px;gap:12px}
.player .bar{flex:1;height:6px;background:#555;border-radius:3px}
.player .bar i{display:block;width:30%;height:100%;background:var(--gold);border-radius:3px}
.pic-grid{position:absolute;left:30px;top:80px;width:300px;display:grid;grid-template-columns:1fr 1fr;gap:12px}
.pic-grid .art{height:136px;border:3px solid var(--white)}
.pic-feature{position:absolute;left:350px;top:80px;width:460px;height:284px;border:4px solid var(--white)}
.site-footer{left:0;top:2112px;width:1200px;height:60px;background:var(--footer);color:var(--white);font-size:11px;padding:22px 0 0 180px}
</style>
</head>
<body>

<nav class="site-nav abs">
  <a class="nav-item"><svg viewBox="0 0 34 30"><path d="M4 15 17 4l13 11h-4v12h-6v-8h-6v8H8V15z" fill="#3aa6e0"/></svg>Home</a>
  <a class="nav-item"><svg viewBox="0 0 34 30"><path d="M3 6h13v20H3zM18 6h13v20H18z" fill="#f0b323"/></svg>Short Stories</a>
  <a class="nav-item"><svg viewBox="0 0 34 30"><rect x="3" y="8" width="28" height="18" rx="2" fill="#6a4fa8"/><path d="M3 8l6-6h4l-6 6zm10 0 6-6h4l-6 6z" fill="#6a4fa8"/></svg>Movies</a>
  <a class="nav-item"><svg viewBox="0 0 34 30"><rect x="3" y="4" width="28" height="22" rx="2" fill="#d23b3b"/><path d="M7 22l7-9 5 6 3-3 6 6z" fill="#fff"/></svg>Picture Stories</a>
</nav>

<div class="social abs">
  <span style="background:var(--social-a)"></span>
  <span style="background:var(--social-b)"></span>
  <span style="background:var(--social-c)"></span>
</div>

<div class="brand abs"><span class="brand-name">Pumblewok</span></div>

<form class="signup abs">
  <div class="signup-bar">
    <div class="signup-label">Add you e-mail for updates</div>
    <div class="signup-input"></div>
    <div class="signup-go">GO</div>
  </div>
  <div class="mascot left" role="img" aria-label="Cartoon boy mascot in white cap"></div>
  <div class="mascot right" role="img" aria-label="Cartoon girl mascot in blue headscarf"></div>
</form>

<section class="panel stories abs">
  <h2>Short Stories</h2>
  <div class="thumb-grid">
    <div class="thumb"><div class="art" role="img" aria-label="Story illustration, desert scene" style="background:linear-gradient(135deg,#e9b86a,#b9743a)"></div><span class="caption">The Quiet Traveller</span></div>
    <div class="thumb"><div class="art" role="img" aria-label="Story illustration, market stall" style="background:linear-gradient(135deg,#c99560,#7d5a3a)"></div><span class="caption">The Art of Patience</span></div>
    <div class="thumb"><div class="art" role="img" aria-label="Story illustration, open book" style="background:linear-gradient(135deg,#9fc9e4,#5d8fb8)"></div><span class="caption">My Book of Kindness</span></div>
    <div class="thumb"><div class="art" role="img" aria-label="Story illustration, night sky" style="background:linear-gradient(135deg,#3c6aa8,#1d3562)"></div><span class="caption">The Starry Night</span></div>
  </div>
  <div class="feature">
    <div class="art" role="img" aria-label="Featured story scene, child in a sunny room" style="background:linear-gradient(160deg,#8fd0ef,#f3d99a 60%,#e9a04d)"></div>
    <div class="caption">Light is every where</div>
  </div>
  <div class="dots" style="top:388px"><i class="on"></i><i></i><i></i></div>
</section>

<section class="panel movies abs">
  <h2>Movies</h2>
  <div class="movie-list">
    <div class="movie">
      <div class="poster" role="img" aria-label="Movie poster, desert caravan" style="background:linear-gradient(180deg,#e7c06a,#9a6a2e)"></div>
      <div>
        <h3>Lantern Hill:<br>A Gift to Everyone</h3>
        <div class="price"><span>PRICE:</span><span>$10.00</span></div>
        <div class="actions"><span class="btn">Trailer</span><span class="btn buy">Buy</span></div>
      </div>
    </div>
    <div class="movie">
      <div class="poster" role="img" aria-label="Movie poster, river and boat" style="background:linear-gradient(180deg,#d89a4e,#6b4a2a)"></div>
      <div>
        <h3>The Story of<br>the River Boat</h3>
        <div class="price"><span>PRICE:</span><span>$10.00</span></div>
        <div class="actions"><span class="btn">Trailer</span><span class="btn buy">Buy</span></div>
      </div>
    </div>
  </div>
  <div class="player">
    <div class="art" role="img" aria-label="Movie trailer frame, figure standing outdoors"></div>
    <div class="notice">Visit our website<br><b>www.pumblewok.net</b><br>for Stories, Games, eCards and more.</div>
    <div class="controls">
      <svg width="14" height="16" viewBox="0 0 14 16"><path d="M1 1l12 7-12 7z" fill="#fff"/></svg>
      <div class="bar"><i></i></div>
      <svg width="18" height="14" viewBox="0 0 18 14"><path d="M1 5h4l5-4v12l-5-4H1z" fill="#fff"/></svg>
    </div>
  </div>
</section>

<section class="panel pictures abs">
  <h2>Picture Stories</h2>
  <div class="pic-grid">
    <div class="art" role="img" aria-label="Picture story cover, elder and child" style="background:linear-gradient(180deg,#f3e3bd,#c9a16b)"></div>
    <div class="art" role="img" aria-label="Picture story cover, travellers" style="background:linear-gradient(180deg,#f0dfb6,#b98c55)"></div>
    <div class="art" role="img" aria-label="Picture story cover, village" style="background:linear-gradient(180deg,#efddb4,#a77c48)"></div>
    <div class="art" role="img" aria-label="Picture story cover, donkey ride" style="background:linear-gradient(180deg,#f1e0b8,#b48850)"></div>
  </div>
  <div class="pic-feature" role="img" aria-label="Featured picture story, Wise Words, town scene with a donkey" style="background:linear-gradient(180deg,#f4e6c4,#d8b47a 65%,#9a7040)"></div>
  <div class="dots" style="top:378px"><i class="on"></i><i></i><i></i></div>
</section>

<footer class="site-footer abs">© 2014 Pumblewok</footer>

</body>
</html>
```